Creative & Professional Business Card for hair salon

We are looking to update our business cards. Our salon is creative, modern, progressive and professional and looking for a design that will reflect this.

```html
<!DOCTYPE html>
<html lang="en">
<head>
<meta charset="utf-8">
<title>Silver Mist Studio – Business Card</title>
<link rel="stylesheet" href="https://fonts.googleapis.com/css2?family=Lato:wght@300;400;700&display=swap">
<style>
  :root{
    --teal:#5d9cb2;
    --teal-soft:#6ea3b1;
    --grey-band:#b9bec2;
    --ink:#555a5e;
    --line:#6a9fb3;
    --card:#ffffff;
    --stage:#e4e6e8;
  }
  *{box-sizing:border-box;margin:0;padding:0}
  html,body{width:1200px;height:900px;overflow:hidden;background:var(--stage)}
  body{font-family:"Lato",sans-serif;color:var(--ink);position:relative}
  .card{
    position:absolute;left:260px;width:680px;height:400px;
    background:var(--card);border-radius:26px;overflow:hidden;
    box-shadow:0 6px 18px rgba(0,0,0,.12);
  }
  .card--front{top:40px}
  .card--back{top:460px}

  /* front */
  .wave{position:absolute;left:0;bottom:0;width:680px;height:400px}
  .brand{position:absolute;left:60px;top:110px;color:var(--teal-soft)}
  .brand__name{font-size:34px;font-weight:300;letter-spacing:.5px;display:block}
  .brand__by{font-size:17px;font-weight:300;display:block;margin-top:4px;padding-left:120px}
  .divider{position:absolute;left:380px;top:60px;width:2px;height:200px;background:var(--line)}
  .contact{position:absolute;left:408px;top:62px;font-size:16px;line-height:1.3}
  .contact__name{color:var(--teal);font-size:24px;font-weight:700;line-height:1.2}
  .contact__role{margin-bottom:2px}
  .contact__address{margin-bottom:8px}
  .contact__row{display:flex;align-items:center;gap:8px}
  .contact__row svg{width:12px;height:12px;flex:none}

  /* back */
  .card--back .brand{left:auto;right:56px;top:36px;text-align:right}
  .card--back .brand__name{font-size:30px}
  .card--back .brand__by{padding-left:0;font-size:15px}
  .appt-title{position:absolute;left:40px;right:40px;top:150px;display:flex;align-items:center;gap:18px;
    color:var(--teal);font-size:22px;font-weight:400}
  .appt-title::before,.appt-title::after{content:"";flex:1;height:2px;background:var(--line)}
  .appt{position:absolute;left:40px;right:40px;top:206px;display:flex;flex-direction:column;gap:22px;font-size:18px}
  .appt__row{display:flex;align-items:flex-end;gap:8px;white-space:nowrap}
  .blank{display:inline-block;height:1px;background:#8a8f93;margin-bottom:5px}
  .blank--name{width:120px}
  .blank--date{width:80px}
  .blank--time{width:70px}
  .check{display:inline-flex;align-items:center;gap:4px;margin-left:6px}
  .check::before{content:"";width:14px;height:14px;border:1.5px solid var(--teal);display:inline-block}
</style>
</head>
<body>

<section class="card card--front" aria-label="Business card front">
  <svg class="wave" viewBox="0 0 680 400" aria-hidden="true">
    <path d="M0 220 C 140 230, 240 280, 320 340 S 470 400, 500 400 L0 400 Z" fill="var(--grey-band)"/>
    <path d="M0 232 C 130 244, 230 292, 305 350 S 450 400, 485 400 L0 400 Z" fill="#fff"/>
    <path d="M0 240 C 120 252, 220 300, 295 356 S 440 400, 470 400 L0 400 Z" fill="var(--teal)"/>
  </svg>
  <div class="brand">
    <span class="brand__name">Silver Mist Studio</span>
    <span class="brand__by">by Tara Lenn</span>
  </div>
  <div class="divider"></div>
  <div class="contact">
    <div class="contact__name">Tara Lenn</div>
    <div class="contact__role">Founder</div>
    <div class="contact__address">5/21 Marlin Avenue,<br>Coralby</div>
    <div class="contact__row">
      <svg viewBox="0 0 12 12"><path d="M3 1 L5 3 L4 4.5 Q5 7 7.5 8 L9 7 L11 9 L9.5 11 Q3 10 1 2.5 Z" fill="var(--teal)"/></svg>
      07 5012 3489
    </div>
    <div class="contact__row">
      <svg viewBox="0 0 12 12"><rect x="1" y="2.5" width="10" height="7" fill="none" stroke="var(--teal)"/><path d="M1 2.5 L6 6.5 L11 2.5" fill="none" stroke="var(--teal)"/></svg>
      salon@silvermiststudio.com.au
    </div>
    <div class="contact__row">
      <svg viewBox="0 0 12 12"><circle cx="6" cy="6" r="5" fill="none" stroke="var(--teal)"/><path d="M1 6 H11 M6 1 V11" stroke="var(--teal)"/></svg>
      www.silvermiststudio.com.au
    </div>
    <div class="contact__row">
      <svg viewBox="0 0 12 12"><circle cx="6" cy="6" r="5" fill="var(--teal)"/></svg>
      SilverMistStudioTaraLenn
    </div>
  </div>
</section>

<section class="card card--back" aria-label="Business card back">
  <div class="brand">
    <span class="brand__name">Silver Mist Studio</span>
    <span class="brand__by">by Tara Lenn</span>
  </div>
  <div class="appt-title">Your Next Appointment</div>
  <div class="appt">
    <div class="appt__row">Name : <span class="blank blank--name"></span> Date : <span class="blank blank--date"></span> Time : <span class="blank blank--time"></span><span class="check">AM</span><span class="check">PM</span></div>
    <div class="appt__row">Name : <span class="blank blank--name"></span> Date : <span class="blank blank--date"></span> Time : <span class="blank blank--time"></span><span class="check">AM</span><span class="check">PM</span></div>
    <div class="appt__row">Name : <span class="blank blank--name"></span> Date : <span class="blank blank--date"></span> Time : <span class="blank blank--time"></span><span class="check">AM</span><span class="check">PM</span></div>
  </div>
</section>

</body>
</html>
```